Poster for the 'LFS Weekly Raffle'

We are a parents association for a senior school and have a number of money raising activities.

We require a poster a lucky draw where parents who subscribe £20 for the school year are entered into a monthly cash prize draw.

Draws are performed monthly. Some detail about it is available here

http://www.larkfield.exampleschool.uk/lfs/about-the-400-society

We are changing the name from 'The 400 society' to 'LFS Weekly raffle', although we don't need the name change highlighted or noted on the poster

A logo is available on the word document application at the above link. Not sure of the quality. I can look to obtain a better resolution, but no promises.

A brief overview of the LFS can be read here for any thoughts / inspiration.

We don't want any reference to specific items purchased, unless we can easily update this on the poster ourselves.

http://www.larkfield.exampleschool.uk/lfs

Target Market(s)

Parents of school kids aged 13 to 17 from whom we are trying to raise contributions to so as to provide funding to school departments who have need to additional items that are not available via the school budget.

Industry/Entity Type

School

Requirements
Must have
• LFS Parents association logo, as in the current 400 society application, should appear.
• Reference to the amount to be contributed of £20 for the year.
• Reference to the monthly prize draw amounts of
• 1st prize - £30
• 2nd prize - £20
• 3rd Prize £10
• Please note all spellings are to be UK english, not American english.
• Payment methods should be highlighted being
• - Brendlo- via the school website
• - Cash
• - Cheque - Payable to Larkfield's Families' Society 400 Society
• No specific colour scheme, although you will see from the school website what the colours are and this should have some representation, but not overbearing.
• The following text is to appear
• The LFS Weekly Raffle is a fundraiser for the Larkfield' Family Society. We raise funds to provide the best possible resources and facilities, for your children, to enhance their learning.
• Thank you for your support of the LFS
Nice to have
• The font type is not to critical, however, it should be easy to read in a short space of time as people are walking past, so not excessive amounts of text detail and not to small a font.

```html
<!DOCTYPE html>
<html lang="en-GB">
<head>
<meta charset="utf-8">
<title>The LFS Weekly Raffle</title>
<link rel="stylesheet" href="https://fonts.googleapis.com/css2?family=Playfair+Display:wght@400;700&family=Libre+Baskerville:wght@400;700&display=swap">
<style>
  :root {
    --maroon-deep: #5e0d12;
    --maroon: #6e1118;
    --prize-first: #74121a;
    --prize-second: #932026;
    --prize-third: #b4232b;
    --band-grey: #cfcdca;
    --panel-light: #efefef;
    --ink: #1e1e1e;
    --paper: #f5f3f1;
    --backdrop: #e4e4e6;
  }
  * { box-sizing: border-box; margin: 0; padding: 0; }
  html, body { width: 1200px; height: 1200px; overflow: hidden; }
  body {
    background: var(--backdrop);
    display: flex; align-items: center; justify-content: center;
    font-family: "Libre Baskerville", Georgia, serif;
    color: var(--ink);
  }
  .poster {
    width: 800px; height: 1130px;
    display: flex; flex-direction: column;
    box-shadow: 0 6px 24px rgba(0,0,0,.18);
  }
  .masthead {
    height: 300px;
    background: radial-gradient(ellipse at 70% 40%, #7b1820 0%, var(--maroon) 45%, var(--maroon-deep) 100%);
    display: flex; align-items: center; padding: 0 40px 0 44px; gap: 40px;
  }
  .club-name {
    width: 190px; display: flex; flex-direction: column; align-items: center; gap: 14px;
    font-family: "Playfair Display", Georgia, serif; font-weight: 700;
    color: var(--paper); font-size: 21px; line-height: 1.2; text-align: center;
  }
  .club-name .mark { width: 70px; height: 70px; border-radius: 50%; background: var(--paper); }
  .title {
    font-family: "Playfair Display", Georgia, serif; font-weight: 400;
    color: var(--paper); font-size: 76px; line-height: 1.08; letter-spacing: .5px;
  }
  .intro {
    height: 110px; background: var(--band-grey);
    display: flex; align-items: center; padding: 0 56px;
    font-weight: 700; font-size: 22px; line-height: 1.45;
  }
  .prizes {
    height: 380px;
    background: linear-gradient(180deg, #f4f4f4 0%, var(--panel-light) 100%);
    position: relative; padding: 34px 0 0 60px;
  }
  .prizes-label {
    font-family: "Playfair Display", Georgia, serif;
    color: var(--prize-second); font-size: 40px; font-weight: 400;
  }
  .prize-list { position: absolute; left: 270px; top: 32px; list-style: none; }
  .prize {
    width: 430px; height: 84px; margin-bottom: 26px;
    display: flex; align-items: center; justify-content: center;
    font-family: "Playfair Display", Georgia, serif;
    color: var(--paper); font-size: 46px;
  }
  .prize sup { font-size: 26px; vertical-align: 18px; }
  .prize--first { background: var(--prize-first); }
  .prize--second { background: var(--prize-second); margin-left: 14px; }
  .prize--third { background: var(--prize-third); margin-left: 28px; }
  .payment {
    height: 150px; background: var(--band-grey);
    padding: 22px 0 0 66px; font-size: 18px;
  }
  .payment h2 { font-size: 18px; font-weight: 400; margin-bottom: 8px; }
  .payment ul { list-style: none; }
  .payment li { line-height: 1.55; font-size: 19px; }
  .payment li::before { content: "\2022"; margin-right: 8px; }
  .closing {
    flex: 1;
    background: radial-gradient(ellipse at 40% 60%, #761720 0%, var(--maroon) 50%, var(--maroon-deep) 100%);
    color: var(--paper); padding: 26px 56px 0 54px;
    font-size: 19px; line-height: 1.5; position: relative;
  }
  .closing p + p { margin-top: 12px; }
  .web {
    position: absolute; left: 0; right: 0; bottom: 16px;
    text-align: center; font-size: 12px; letter-spacing: .3px;
  }
</style>
</head>
<body>
  <article class="poster">
    <header class="masthead">
      <div class="club-name">
        <span class="mark"></span>
        <span>Larkfield School<br>Families' Society</span>
      </div>
      <h1 class="title">The LFS<br>Weekly Raffle</h1>
    </header>

    <section class="intro">
      <p>Parents who subscribe £20 for the school year are entered into a monthly cash prize draw.</p>
    </section>

    <section class="prizes">
      <h2 class="prizes-label">Prizes:</h2>
      <ul class="prize-list">
        <li class="prize prize--first">1<sup>st</sup>&nbsp;- £30</li>
        <li class="prize prize--second">2<sup>nd</sup>&nbsp;- £20</li>
        <li class="prize prize--third">3<sup>rd</sup>&nbsp;- £10</li>
      </ul>
    </section>

    <section class="payment">
      <h2>Payment methods :</h2>
      <ul>
        <li>Brendlo- via the school website</li>
        <li>Cash</li>
        <li>Cheque - Payable to Larkfield's Families' Society 400 Society</li>
      </ul>
    </section>

    <footer class="closing">
      <p>The LFS Weekly Raffle is a fundraiser for the Larkfield' Family Society. We raise funds to provide the best possible resources and facilities, for your children, to enhance their learning.</p>
      <p>Thank you for your support of the LFS</p>
      <p class="web">www.larkfield.exampleschool.uk</p>
    </footer>
  </article>
</body>
</html>
```